Aisle signage for supermarket

Design Isle signs for Indian supermarket. Modern, Clear, legible. Would be nice to use our logo colours. Signs Will be double sided and measure 900mm width x 400mm height. Indian theme would be nice. Attached files shows description to go on each sign.
Font styles to use
Sans Serif
Colors
Designer to choose colors to be used in the design.

```html
<!DOCTYPE html>
<html lang="en">
<head>
<meta charset="utf-8">
<title>Aisle Signage</title>
<link rel="stylesheet" href="https://fonts.googleapis.com/css2?family=Montserrat:wght@800;900&display=swap">
<style>
  :root {
    --bg-light: #b3d789;
    --bg-dark: #8cc24a;
    --panel-dark: #0b6a33;
    --panel-mid: #2b8a3a;
    --panel-light: #4a9e3c;
    --badge: #231f20;
    --ink: #ffffff;
    --brand: #1e6b34;
    --fade: #e6efe0;
  }
  * { margin: 0; padding: 0; box-sizing: border-box; }
  html, body { width: 720px; height: 1200px; overflow: hidden; }
  body {
    background: linear-gradient(160deg, var(--bg-light) 0%, #a2cf6c 50%, var(--bg-dark) 100%);
    font-family: "Montserrat", sans-serif;
    position: relative;
  }
  .sign {
    position: absolute;
    overflow: hidden;
    background: linear-gradient(120deg, var(--panel-dark) 0%, var(--panel-mid) 55%, var(--panel-light) 100%);
    box-shadow: -8px 14px 18px rgba(30, 60, 10, 0.45);
  }
  .sign--feature { left: 60px; top: 57px; width: 600px; height: 267px; }
  .sign--aisle { width: 287px; height: 128px; }
  .col-left { left: 60px; }
  .col-right { left: 373px; }
  .row-1 { top: 359px; }
  .row-2 { top: 523px; }
  .row-3 { top: 687px; }
  .row-4 { top: 851px; }
  .row-5 { top: 1015px; }

  .sign__art {
    position: absolute;
    right: 0; top: 0; bottom: 0;
    background: radial-gradient(circle at 40% 55%, rgba(20, 60, 25, 0.18), rgba(20, 60, 25, 0) 70%);
  }
  .sign--feature .sign__art { width: 230px; }
  .sign--aisle .sign__art { width: 110px; }

  .sign__brandzone {
    position: absolute;
    right: 0; bottom: 0;
    background: linear-gradient(180deg, rgba(230, 239, 224, 0) 0%, var(--fade) 55%);
    display: flex; align-items: flex-end; justify-content: center;
  }
  .sign--feature .sign__brandzone { width: 117px; height: 86px; padding-bottom: 14px; }
  .sign--aisle .sign__brandzone { width: 56px; height: 36px; padding-bottom: 6px; }
  .brand {
    color: var(--brand);
    font-weight: 800;
    letter-spacing: 0.12em;
    white-space: nowrap;
  }
  .sign--feature .brand { font-size: 13px; }
  .sign--aisle .brand { font-size: 6.5px; }

  .badge {
    position: absolute;
    border-radius: 50%;
    background: var(--badge);
    color: var(--ink);
    font-weight: 900;
    display: flex; align-items: center; justify-content: center;
  }
  .sign--feature .badge { width: 144px; height: 144px; left: 457px; top: -10px; font-size: 96px; padding-left: 6px; }
  .sign--aisle .badge { width: 68px; height: 68px; left: 220px; top: 0; font-size: 40px; }

  .items { position: absolute; list-style: none; color: var(--ink); font-weight: 800; }
  .items li { position: relative; }
  .items li::before {
    content: ""; position: absolute; border-radius: 50%; background: var(--ink);
  }
  .sign--feature .items { left: 35px; top: 36px; font-size: 34px; line-height: 52px; }
  .sign--feature .items li { padding-left: 25px; }
  .sign--feature .items li::before { width: 9px; height: 9px; left: 1px; top: 22px; }
  .sign--aisle .items { left: 17px; top: 14px; font-size: 15.5px; line-height: 25px; letter-spacing: 0.01em; }
  .sign--aisle .items li { padding-left: 12px; }
  .sign--aisle .items li::before { width: 4.5px; height: 4.5px; left: 0; top: 11px; }
</style>
</head>
<body>

<section class="sign sign--feature">
  <div class="sign__art" role="img" aria-label="Line drawings of Indian dishes, samosas and spices"></div>
  <div class="sign__brandzone"><span class="brand">TARANG FOODS</span></div>
  <div class="badge">1</div>
  <ul class="items">
    <li>SAVOURIES</li>
    <li>BISCUITS /<br>CAKES</li>
    <li>TEA / COFFEE</li>
  </ul>
</section>

<section class="sign sign--aisle col-left row-1">
  <div class="sign__art" role="img" aria-label="Line drawings of Indian dishes"></div>
  <div class="sign__brandzone"><span class="brand">TARANG</span></div>
  <div class="badge">1</div>
  <ul class="items"><li>JUICES</li><li>SOFT DRINKS</li></ul>
</section>

<section class="sign sign--aisle col-right row-1">
  <div class="sign__art" role="img" aria-label="Line drawings of Indian dishes"></div>
  <div class="sign__brandzone"><span class="brand">TARANG</span></div>
  <div class="badge">1</div>
  <ul class="items"><li>FROZEN</li><li>DESSERT MIXES</li><li>TABLE / COOKING<br>SAUCES</li></ul>
</section>

<section class="sign sign--aisle col-left row-2">
  <div class="sign__art" role="img" aria-label="Line drawings of Indian dishes"></div>
  <div class="sign__brandzone"><span class="brand">TARANG</span></div>
  <div class="badge">2</div>
  <ul class="items"><li>DRY FRUITS /<br>NUTS</li><li>LENTILS / DALL</li></ul>
</section>

<section class="sign sign--aisle col-right row-2">
  <div class="sign__art" role="img" aria-label="Line drawings of Indian dishes"></div>
  <div class="sign__brandzone"><span class="brand">TARANG</span></div>
  <div class="badge">2</div>
  <ul class="items"><li>WHOLE SPICES</li><li>GROUND SPICES</li></ul>
</section>

<section class="sign sign--aisle col-left row-3">
  <div class="sign__art" role="img" aria-label="Line drawings of Indian dishes"></div>
  <div class="sign__brandzone"><span class="brand">TARANG</span></div>
  <div class="badge">2</div>
  <ul class="items"><li>FLOURS</li><li>RICE</li></ul>
</section>

<section class="sign sign--aisle col-right row-3">
  <div class="sign__art" role="img" aria-label="Line drawings of Indian dishes"></div>
  <div class="sign__brandzone"><span class="brand">TARANG</span></div>
  <div class="badge">3</div>
  <ul class="items"><li>PASTA /<br>VERMICELLI</li><li>OLIVES</li><li>HONEY</li></ul>
</section>

<section class="sign sign--aisle col-left row-4">
  <div class="sign__art" role="img" aria-label="Line drawings of Indian dishes"></div>
  <div class="sign__brandzone"><span class="brand">TARANG</span></div>
  <div class="badge">3</div>
  <ul class="items"><li>OILS / GHEE</li><li>CANNED<br>PRODUCTS</li></ul>
</section>

<section class="sign sign--aisle col-right row-4">
  <div class="sign__art" role="img" aria-label="Line drawings of Indian dishes"></div>
  <div class="sign__brandzone"><span class="brand">TARANG</span></div>
  <div class="badge">3</div>
  <ul class="items"><li>INCENSE</li><li>DISPOSABLES</li><li>HOUSEHOLD /<br>LAUNDRY</li></ul>
</section>

<section class="sign sign--aisle col-left row-5">
  <div class="sign__art" role="img" aria-label="Line drawings of Indian dishes"></div>
  <div class="sign__brandzone"><span class="brand">TARANG</span></div>
  <div class="badge">4</div>
  <ul class="items"><li>CHILLED FOODS</li><li>JAGGERY</li></ul>
</section>

<section class="sign sign--aisle col-right row-5">
  <div class="sign__art" role="img" aria-label="Line drawings of Indian dishes"></div>
  <div class="sign__brandzone"><span class="brand">TARANG</span></div>
  <div class="badge">4</div>
  <ul class="items"><li>NAAN / BREAD</li><li>TOILETRIES</li></ul>
</section>

</body>
</html>
```